Design a Label for Essential Oil Bottle

Need help designing the label for the 10 ML Essential Oil bottle. The label should include the following:

Corvane 8:22 ( This is the Brand)
Essential Oil
100% Pure Therapeutic Quality
Storage: Keep in a cool, dark place

```html
<!DOCTYPE html>
<html lang="en">
<head>
<meta charset="utf-8">
<title>Corvane 8:22 Essential Oil Label</title>
<link rel="stylesheet" href="https://fonts.googleapis.com/css2?family=Poppins:wght@300;400;500;600&display=swap">
<style>
  :root {
    --canvas-bg: #ececec;
    --label-black: #050505;
    --pattern-tone: #1d1d1d;
    --teal: #0bb7aa;
    --ink: #111111;
    --white: #ffffff;
  }
  html, body {
    margin: 0;
    padding: 0;
    width: 960px;
    height: 1200px;
    overflow: hidden;
    background: var(--canvas-bg);
  }
  .canvas {
    position: relative;
    width: 960px;
    height: 1200px;
  }
  .label {
    position: absolute;
    left: 40px;
    top: 364px;
    width: 880px;
    height: 472px;
    font-family: "Poppins", sans-serif;
  }
  .label-base { fill: var(--label-black); }
  .pattern-band { fill: var(--pattern-tone); }
  .teal-panel { fill: var(--teal); }
  .drop { fill: var(--label-black); }
  .brand-name { fill: var(--white); font-size: 25px; font-weight: 400; }
  .volume { fill: var(--white); font-size: 25px; font-weight: 500; letter-spacing: 1px; }
  .purity-number { fill: var(--white); font-size: 41px; font-weight: 300; }
  .purity-word { fill: var(--white); font-size: 18px; font-weight: 400; }
  .product-name { fill: var(--ink); font-size: 38px; font-weight: 500; letter-spacing: 0.5px; }
  .quality { fill: var(--white); font-size: 22px; font-weight: 400; letter-spacing: 1px; }
  .storage-title { fill: var(--white); font-size: 16px; font-weight: 600; }
  .storage-text { fill: var(--white); font-size: 16px; font-weight: 400; }
</style>
</head>
<body>
<div class="canvas">
  <svg class="label" viewBox="0 0 880 472" xmlns="http://www.w3.org/2000/svg">
    <rect class="label-base" x="0" y="0" width="880" height="472"/>
    <rect class="pattern-band" role="img" aria-label="Dark olive branch pattern band" x="0" y="0" width="880" height="68"/>
    <rect class="pattern-band" role="img" aria-label="Dark olive branch pattern band" x="0" y="401" width="880" height="71"/>

    <rect class="teal-panel" x="0" y="68" width="524" height="333"/>
    <rect class="teal-panel" x="624" y="68" width="145" height="333"/>
    <rect class="label-base" x="769" y="68" width="111" height="333"/>
    <rect class="label-base" x="524" y="68" width="100" height="333"/>

    <path class="drop" d="M347,30 C372,75 434,100 434,138 A87,87 0 0 1 260,138 C260,100 322,75 347,30 Z"/>
    <text class="brand-name" x="347" y="161" text-anchor="middle">CORVANE 8:22</text>

    <text class="volume" transform="translate(45 257) rotate(90)" text-anchor="middle">10 ML</text>

    <text x="270" y="302"><tspan class="purity-number">100%</tspan><tspan class="purity-word" dx="4">Pure</tspan></text>
    <text class="product-name" x="270" y="342">ESSENTIAL</text>
    <text class="product-name" x="270" y="382">OIL</text>

    <text class="quality" transform="translate(586 238) rotate(-90)" text-anchor="middle">THERAPEUTIC QUALITY</text>

    <text class="storage-title" transform="translate(800 148) rotate(90)">STORAGE:</text>
    <text class="storage-text" transform="translate(780 148) rotate(90)">Keep in a cool, dark place</text>
  </svg>
</div>
</body>
</html>
```